Business Card Design for company

We want new business cards. We'd like something different-- yet still highly professional. Our tagline is Providing leadership, delivering success. Stock photos are ok, as long as they are relevant and look upscale.

Target Market(s)

Architecture/Business Management Consulting/Engineering Consulting

Contact Information for Business Card

dark gray background with pops of blue might be good, but you tell me. You're the designers. Rounded corners might be nice, but again, you tell me.

Font styles to use
Serif
Sans Serif

Colors
3276b5
5c5c5c
9d9d9d
fbfbfb

Requirements
Nice to have
• Something different, but still very professional.

```html
<!DOCTYPE html>
<html lang="en">
<head>
<meta charset="UTF-8">
<title>Corvane Partners – Business Card</title>
<link href="https://fonts.googleapis.com/css2?family=Montserrat:wght@400;600;700&family=Arimo:wght@400&display=swap" rel="stylesheet">
<style>
  :root {
    --page-bg: #e6e7e9;
    --card-front: #5f6268;
    --card-front-top: #54575c;
    --card-back: #0f0f10;
    --card-back-top: #1a1a1b;
    --accent-blue: #3276b5;
    --text-light: #fbfbfb;
    --rule: #f2f2f2;
  }
  * { box-sizing: border-box; margin: 0; padding: 0; }
  html, body { width: 1200px; height: 900px; overflow: hidden; }
  body {
    background: var(--page-bg);
    display: flex;
    align-items: center;
    justify-content: center;
    gap: 60px;
    font-family: "Arimo", Arial, sans-serif;
  }
  .card {
    position: relative;
    width: 520px;
    height: 300px;
    border-radius: 22px;
    overflow: hidden;
    box-shadow: 0 10px 28px rgba(0,0,0,0.22);
  }
  .card-front {
    background: linear-gradient(160deg, var(--card-front-top), var(--card-front));
    color: var(--text-light);
  }
  .card-back {
    background: linear-gradient(160deg, var(--card-back-top), var(--card-back));
    display: flex;
    align-items: center;
    justify-content: center;
  }
  .person {
    position: absolute;
    left: 36px;
    top: 34px;
  }
  .person-name {
    font-family: "Montserrat", sans-serif;
    font-weight: 700;
    font-size: 13px;
    letter-spacing: 0.5px;
    text-transform: uppercase;
  }
  .person-title {
    font-family: "Montserrat", sans-serif;
    font-weight: 400;
    font-size: 11px;
    color: var(--accent-blue);
    text-transform: uppercase;
    margin-top: 2px;
  }
  .brand-name {
    font-family: "Montserrat", sans-serif;
    font-weight: 600;
    text-transform: uppercase;
    line-height: 1;
  }
  .card-front .brand-name {
    position: absolute;
    right: 40px;
    top: 96px;
    font-size: 40px;
    text-align: right;
    color: var(--text-light);
  }
  .card-front .brand-name small {
    display: block;
    font-size: 15px;
    letter-spacing: 3px;
    margin-top: 6px;
  }
  .card-back .brand-name {
    font-size: 46px;
    color: var(--accent-blue);
    text-align: center;
  }
  .card-back .brand-name small {
    display: block;
    font-size: 15px;
    letter-spacing: 4px;
    margin-top: 8px;
  }
  .divider {
    position: absolute;
    left: 36px;
    right: 120px;
    top: 178px;
    height: 1px;
    background: var(--rule);
  }
  .contact-list {
    position: absolute;
    left: 36px;
    top: 192px;
    list-style: none;
    font-size: 13px;
    line-height: 19px;
  }
  .contact-list li { display: flex; align-items: center; gap: 8px; }
  .contact-list svg { width: 12px; height: 12px; flex: none; }
  .address {
    position: absolute;
    right: 40px;
    bottom: 26px;
    text-align: right;
    font-size: 14px;
    line-height: 19px;
  }
</style>
</head>
<body>
  <section class="card card-front">
    <div class="person">
      <p class="person-name">Daniel Marlowe</p>
      <p class="person-title">CEO/Founder</p>
    </div>
    <p class="brand-name">Corvane<small>Partners</small></p>
    <div class="divider"></div>
    <ul class="contact-list">
      <li>
        <svg viewBox="0 0 24 24" fill="#3276b5" aria-hidden="true"><path d="M6.6 10.8a15.1 15.1 0 0 0 6.6 6.6l2.2-2.2a1 1 0 0 1 1-.25 11.4 11.4 0 0 0 3.6.57 1 1 0 0 1 1 1V20a1 1 0 0 1-1 1A17 17 0 0 1 3 4a1 1 0 0 1 1-1h3.5a1 1 0 0 1 1 1c0 1.25.2 2.45.57 3.6a1 1 0 0 1-.25 1z"/></svg>
        230.555.0148
      </li>
      <li>
        <svg viewBox="0 0 24 24" fill="#3276b5" aria-hidden="true"><path d="M2 5h20v14H2z"/><path d="M2 5l10 8 10-8" fill="none" stroke="#5f6268" stroke-width="2"/></svg>
        daniel@corvane.com
      </li>
      <li>
        <svg viewBox="0 0 24 24" fill="none" stroke="#3276b5" stroke-width="2" aria-hidden="true"><circle cx="12" cy="12" r="10"/><path d="M2 12h20M12 2c3 3 3 17 0 20M12 2c-3 3-3 17 0 20"/></svg>
        www.corvanepartners.com
      </li>
    </ul>
    <address class="address" style="font-style:normal">
      4720 Halden Park Dr<br>
      Ste 310, Ridgefield<br>
      NC 28150
    </address>
  </section>

  <section class="card card-back">
    <p class="brand-name">Corvane<small>Partners</small></p>
  </section>
</body>
</html>
```